Seller Looking for a luxurious diverse ethnic look...stunning but not overly seductive

I need a web Design for a company based in NEW YORK CITY called Velvet Harbor LLC. Initially I will be selling clothing and accessories as well as electronics on Tradora and hope to branch out. I want the whole experience for my customers and people I will buy from when they deal with me to be confident that this will be a velvet harbor and luxurious transaction.
Updates

Project Deadline Extended Reason: As I keep getting these great designs I continue to get more ideas and feel more time will help get us there. Added Thursday, July 16, 2015

Target Market(s)

ages 20-60

Industry/Entity Type

Clothing

Number of Pages Required

1 page

Font styles to use
Script

Colors
b768aa

Requirements
Must have
• Sleek and Luxurious feel and modern. I would like the page to look startling stunning yet not overly seductive and to include ethnic diversity. I like the illusion not knowing what the sight is selling since I am not targeting one area.
Should not have
• Do not want it to look generic or traditional

```html
<!DOCTYPE html>
<html lang="en">
<head>
<meta charset="utf-8">
<title>Velvet Harbor — Clothing, Accessories &amp; Electronics</title>
<link rel="stylesheet" href="https://fonts.googleapis.com/css2?family=Courgette&family=Open+Sans:ital,wght@0,400;0,600;1,400&family=Ubuntu:wght@400;500&display=swap">
<style>
:root{
  --plum:#b768aa;
  --plum-deep:#8e3f86;
  --night:#2a1248;
  --violet:#5b2a8c;
  --sand:#e3a857;
  --ink:#4a4a4a;
  --muted:#8a8a8a;
  --line:#e8d9c6;
  --paper:#ffffff;
}
*{box-sizing:border-box;margin:0;padding:0}
html,body{width:769px;height:1200px;overflow:hidden}
body{font-family:"Open Sans",Arial,sans-serif;color:var(--ink);position:relative;
  background:linear-gradient(180deg,#3a1a6a 0%,#6a3aa8 35%,#a05ac0 60%,#3b1e5c 85%,#1c0d30 100%)}
.city-backdrop{position:absolute;inset:0;
  background:radial-gradient(ellipse at 50% 70%,rgba(255,190,240,.35),transparent 60%),
  linear-gradient(180deg,transparent 55%,rgba(20,10,40,.7) 100%)}
.page{position:absolute;left:50px;top:0;width:669px;height:1200px;background:var(--paper);
  box-shadow:0 0 18px rgba(0,0,0,.35)}
.masthead{height:166px;text-align:center;padding-top:28px;
  background:linear-gradient(180deg,#c58ac0 0%,#e8cbe4 45%,#fff 100%)}
.brand-name{font-family:"Courgette",cursive;font-size:50px;color:var(--plum-deep);line-height:1}
.brand-tag{font-family:"Ubuntu",sans-serif;font-size:15px;letter-spacing:1px;color:var(--plum-deep);margin-top:10px}
.main-nav,.foot-nav{display:flex;justify-content:space-between;border-top:1px solid var(--line);border-bottom:1px solid var(--line);
  margin:0 14px;padding:5px 8px;font-size:9px;letter-spacing:.5px;color:var(--sand);text-transform:uppercase}
.welcome{text-align:center;padding:14px 30px 0}
.welcome h1{font-family:"Ubuntu",sans-serif;font-weight:400;font-size:20px;color:var(--sand)}
.welcome-cols{display:flex;gap:30px;margin-top:8px}
.welcome-col{flex:1;font-size:11px;line-height:1.45;text-align:center}
.btn{display:inline-block;margin-top:9px;padding:5px 22px;border:1px solid #bbb;border-radius:4px;font-size:11px;font-weight:600;
  background:linear-gradient(#fff,#eee);color:var(--ink)}
.collections{display:flex;gap:22px;padding:20px 32px 0}
.collection{flex:1}
.collection-photo{height:100px;border-radius:10px;padding:14px 18px;color:#fff;
  background:linear-gradient(135deg,#c9c2bb,#8f857c 60%,#6d625a)}
.collection-photo.men{background:linear-gradient(135deg,#d8d3cf,#a69b92 55%,#7d7168)}
.collection-photo h2{font-family:"Ubuntu",sans-serif;font-weight:400;font-size:22px}
.collection-photo p{font-size:10px;width:60%;margin-top:2px}
.collection-text{font-size:9.5px;line-height:1.5;margin-top:8px;color:var(--muted)}
.collection-text p+p{margin-top:8px}
.range{margin:42px 14px 0;border:1px solid var(--line);border-radius:14px;height:220px;padding:12px 16px;position:relative}
.panel-title{font-family:"Ubuntu",sans-serif;font-size:18px;color:var(--sand);display:flex;align-items:baseline;gap:14px}
.panel-title small{font-family:"Open Sans",sans-serif;font-size:9px;color:var(--muted)}
.product-grid{display:grid;grid-template-columns:repeat(6,76px);gap:18px 16px;justify-content:center;margin-top:14px}
.product{height:68px;border:1px solid #eee;background:radial-gradient(circle,#5a5a5a 0%,#2b2b2b 45%,#fff 47%)}
.arrow{position:absolute;top:100px}
.arrow.left{left:8px}.arrow.right{right:8px}
.testimonials{margin:60px 14px 0;border:1px solid var(--line);border-radius:14px;height:118px;padding:12px 16px;position:relative}
.quotes{display:flex;gap:30px;margin:16px 30px 0}
.quote{flex:1;display:flex;gap:10px;align-items:flex-start}
.quote-mark{width:42px;height:42px;flex:none;border:1px solid var(--line);border-radius:4px}
.quote p{font-family:"Courgette",cursive;font-size:12px;line-height:1.35;color:var(--ink)}
.quote cite{display:block;text-align:right;font-size:9px;color:var(--muted);font-style:italic;margin-top:3px}
.contact{margin:26px 14px 0;height:152px;border-top:1px solid var(--line);display:flex;align-items:center;justify-content:space-between;padding:0 28px;font-size:9.5px;color:var(--muted)}
.contact ul{list-style:none;display:flex;flex-direction:column;gap:12px}
.contact li{display:flex;align-items:center;gap:8px}
.store-badge{width:130px;height:130px;border-radius:50%;background:#f4eef4;border:1px solid var(--line);
  display:flex;align-items:center;justify-content:center;font-family:"Ubuntu",sans-serif;font-size:24px;color:var(--plum-deep)}
.foot-nav{margin-top:8px}
</style>
</head>
<body>
<div class="city-backdrop" role="img" aria-label="Night skyline of New York City in purple light"></div>
<main class="page">
  <header class="masthead">
    <div class="brand-name">Velvet Harbor</div>
    <div class="brand-tag">CLOTHING, ACCESSORIES &amp; ELECTRONICS</div>
  </header>
  <nav class="main-nav"><span>Mens Clothing</span><span>Womens Clothing</span><span>Jewellery</span><span>Other Accessories</span><span>Electronics</span></nav>

  <section class="welcome">
    <h1>WELCOME TO OUR STORE</h1>
    <div class="welcome-cols">
      <div class="welcome-col">Velvet Harbor brings together graceful clothing, fine accessories and modern electronics under one roof.<br><span class="btn">VIEW RANGE</span></div>
      <div class="welcome-col">Based in New York City, Velvet Harbor offers a calm, refined and personal way to shop.<br><span class="btn">READ MORE</span></div>
    </div>
  </section>

  <section class="collections">
    <article class="collection">
      <div class="collection-photo" role="img" aria-label="Woman modelling an elegant outfit">
        <h2>Womens Clothing</h2><p>Elegant pieces for every occasion and evening.</p>
      </div>
      <div class="collection-text">
        <p>Soft fabrics, clean lines and timeless cuts chosen for women who like quiet luxury. Every garment is checked for fit and finish before it reaches you, so you can dress with confidence.</p>
        <p>New arrivals are added each week. Browse dresses, knitwear and tailored pieces in a range of sizes and colours.</p>
      </div>
    </article>
    <article class="collection">
      <div class="collection-photo men" role="img" aria-label="Man modelling a tailored shirt">
        <h2>Mens Clothing</h2><p>Sharp tailoring for work, travel and evening.</p>
      </div>
      <div class="collection-text">
        <p>Shirts, jackets and trousers selected for comfort and a polished look. Each piece is chosen to pair easily with the rest of your wardrobe and to last season after season.</p>
        <p>Explore classic staples alongside modern details. Sizes run from small to extra large, with fast and careful delivery.</p>
      </div>
    </article>
  </section>

  <section class="range">
    <h2 class="panel-title">Our Range <small>Shop our range: women · men · jewellery · other accessories · electronics</small></h2>
    <div class="product-grid">
      <div class="product" role="img" aria-label="E-reader"></div>
      <div class="product" role="img" aria-label="Projector"></div>
      <div class="product" role="img" aria-label="Camera"></div>
      <div class="product" role="img" aria-label="Media player"></div>
      <div class="product" role="img" aria-label="Streaming stick"></div>
      <div class="product" role="img" aria-label="Smart watch"></div>
      <div class="product" role="img" aria-label="Media box"></div>
      <div class="product" role="img" aria-label="Earphones"></div>
      <div class="product" role="img" aria-label="Car charger"></div>
      <div class="product" role="img" aria-label="Cable"></div>
      <div class="product" role="img" aria-label="Set-top box"></div>
      <div class="product" role="img" aria-label="Game console"></div>
    </div>
    <svg class="arrow left" width="12" height="20" viewBox="0 0 12 20"><path d="M10 2 2 10l8 8" fill="none" stroke="#bbb" stroke-width="2"/></svg>
    <svg class="arrow right" width="12" height="20" viewBox="0 0 12 20"><path d="M2 2l8 8-8 8" fill="none" stroke="#bbb" stroke-width="2"/></svg>
  </section>

  <section class="testimonials">
    <h2 class="panel-title">Customer Testimonials</h2>
    <div class="quotes">
      <div class="quote"><div class="quote-mark" role="img" aria-label="Customer photo"></div><p>Wonderful range, extremely attractive clothing and great fit too!<cite>— Amara K.</cite></p></div>
      <div class="quote"><div class="quote-mark" role="img" aria-label="Customer photo"></div><p>Excellent. Had a wide range of sizes and provided great style advice.<cite>— Lena M.</cite></p></div>
    </div>
    <svg class="arrow left" style="top:58px" width="12" height="20" viewBox="0 0 12 20"><path d="M10 2 2 10l8 8" fill="none" stroke="#bbb" stroke-width="2"/></svg>
    <svg class="arrow right" style="top:58px" width="12" height="20" viewBox="0 0 12 20"><path d="M2 2l8 8-8 8" fill="none" stroke="#bbb" stroke-width="2"/></svg>
  </section>

  <footer>
    <div class="contact">
      <ul>
        <li><svg width="14" height="14"><circle cx="7" cy="7" r="6" fill="none" stroke="#b768aa"/></svg>Follow us on our community page</li>
        <li><svg width="14" height="14"><path d="M7 1l1.8 4 4.2.4-3.2 2.8 1 4.2L7 10.2 3.2 12.4l1-4.2L1 5.4l4.2-.4z" fill="#b768aa"/></svg>Read our reviews on Tradora</li>
        <li><svg width="14" height="14"><rect x="1" y="3" width="12" height="8" fill="none" stroke="#b768aa"/><path d="M1 3l6 5 6-5" fill="none" stroke="#b768aa"/></svg>Send us a message</li>
      </ul>
      <div class="store-badge">Tradora</div>
      <ul>
        <li><svg width="14" height="14"><path d="M7 1a4 4 0 0 1 4 4c0 3-4 8-4 8S3 8 3 5a4 4 0 0 1 4-4z" fill="#b768aa"/></svg>Visit our Tradora store</li>
        <li><svg width="14" height="14"><path d="M3 1h3l1 3-2 1a7 7 0 0 0 4 4l1-2 3 1v3c-6 1-11-4-10-10z" fill="#b768aa"/></svg>(212) 555-0148</li>
        <li><svg width="14" height="14"><rect x="1" y="3" width="12" height="8" fill="none" stroke="#b768aa"/><path d="M1 3l6 5 6-5" fill="none" stroke="#b768aa"/></svg>hello@velvetharbor.example</li>
      </ul>
    </div>
    <nav class="foot-nav"><span>Mens Clothing</span><span>Womens Clothing</span><span>Jewellery</span><span>Other Accessories</span><span>Electronics</span></nav>
  </footer>
</main>
</body>
</html>
```